Art for parenting podcast with straight/direct talk...no fluff here! "Plain Word for Families"

I need an image that will not look fluffy or soft. A no-nonsense look. This is not a 'I love parenting' podcast. It is for frustrated parents who don't know what to do. The name is 'Plain Word for Families'. The design should, therefore, NOT have hearts and flowers but, instead, look clean and direct. My logo has shades of blue so that would be nice. I have done this work for over 30 years and am well-degreed so would like the design to look stable/established. I have attached my company's logo.

Target Market(s)

Frustrated parents of children - age birth to 20

Industry/Entity Type

Coaching/Counseling for parents

Font styles to use
Serif
Sans Serif

Colors
0054AA
0677BA
7BADD7
CADEEF
E8F1F8

Requirements
Must have
• A look that is clean/bold/direct and professional. Serious.
Nice to have
• If it looks good, my name with my degrees behind my name. MS, MEd. Another thought would be to have a background image of a frustrated parent. Not sure if that would be good or look too busy.
Should not have
• Flowers, fluff, soft appearance, pinks, light colors

```html
<!DOCTYPE html>
<html lang="en">
<head>
<meta charset="UTF-8">
<title>Plain Word for Families – Podcast Cover</title>
<link href="https://fonts.googleapis.com/css2?family=Oswald:wght@500;600&display=swap" rel="stylesheet">
<style>
  :root {
    --stage: #e3e4e6;
    --blue-deep: #0054aa;
    --blue-mid: #0677ba;
    --blue-glow: #4f9bd6;
    --white: #ffffff;
    --navy-figure: #15163a;
  }
  * { margin: 0; padding: 0; box-sizing: border-box; }
  html, body {
    width: 1200px; height: 807px; overflow: hidden;
    background: var(--stage);
  }
  .stage { position: relative; width: 1200px; height: 807px; }
  .cover {
    position: absolute; left: 250px; top: 53px;
    width: 700px; height: 700px;
    background: radial-gradient(circle at 78% 58%, var(--blue-glow) 0%, var(--blue-mid) 32%, var(--blue-deep) 78%);
    overflow: hidden;
    font-family: "Oswald", "Arial Narrow", sans-serif;
    color: var(--white);
  }
  .cover-frame {
    position: absolute; inset: 22px;
    border: 5px solid var(--white);
    pointer-events: none;
    z-index: 3;
  }
  .title {
    position: absolute; left: 58px; top: 92px;
    z-index: 2;
    font-size: 90px; font-weight: 600;
    line-height: 1.04;
    letter-spacing: 1px;
    text-transform: uppercase;
  }
  .title-line { display: block; white-space: nowrap; }
  .subtitle {
    position: absolute; left: 0; width: 460px; top: 448px;
    text-align: center;
    font-size: 44px; font-weight: 500; letter-spacing: 2px;
    z-index: 2;
  }
  .brand {
    position: absolute; left: 0; width: 460px; top: 548px;
    display: flex; align-items: center; justify-content: center; gap: 12px;
    z-index: 2;
  }
  .brand-dot {
    width: 22px; height: 22px; border-radius: 50%;
    background: var(--white);
  }
  .brand-name {
    font-size: 28px; font-weight: 500; letter-spacing: 1.5px;
    text-transform: uppercase;
  }
  .figure-area {
    position: absolute; left: 462px; top: 318px;
    width: 211px; height: 355px;
    border-radius: 100px 100px 0 0;
    background: linear-gradient(180deg, #1c1e46 0%, var(--navy-figure) 100%);
    z-index: 1;
  }
</style>
</head>
<body>
  <main class="stage">
    <section class="cover">
      <div class="cover-frame"></div>

      <h1 class="title">
        <span class="title-line">Plain</span>
        <span class="title-line">Word for</span>
        <span class="title-line">Families</span>
      </h1>

      <p class="subtitle">PODCAST</p>

      <div class="brand">
        <span class="brand-dot"></span>
        <span class="brand-name">Keelstone Parenting</span>
      </div>

      <div class="figure-area" role="img" aria-label="Silhouette of a frustrated parent holding their head in their hands"></div>
    </section>
  </main>
</body>
</html>
```